Simple design for eCommerce retailer of Custom Cut Mirror Frames

We need a fresh design for our eCommerce store. Currently, we need a design for each page on the existing site.

Here is the site as it stands right now: glassvela.com

Here is a competitor site that we like. The owner really likes the block look for the home page: framebloom.com

Here is a video we would like to feature: https://vidhost.example/kT7pQm2XrLa

Here is the color palate, emphasis on the green and purple: https://palettebox.example/quiet-evening-hues-theme-48213976/?showPublished=true

Here is an example of a landing page we are currently using: https://glassvela.com/lander-10-off-install/

Font for the site should be the google font Lato

Home page should include the following sections/blocks:

How it works
Shop now
Testimonials
Featured Products
Before and After Gallery
Updates

My team has been slow getting back to me with feedback. I'm pushing them to speed their process up.

Target Market(s)

Women, Ages 35-65+

Number of Pages Required

5+ page

Font styles to use
Sans Serif

Requirements
Must have
• -Before and after gallery
• -Star ratings
• -eCommerce look and feel
• -Info about being able to order free samples
• -Language from the checkmarks on the landing page
• -sleek product page
• -home page should be have a very modern design feel
Should not have
• Product Prices...the user has to use the calculator to determine the price of their purchase.
• Sliders

```html
<!DOCTYPE html>
<html lang="en">
<head>
<meta charset="utf-8">
<title>GlassVela – Custom Mirror Frames</title>
<link href="https://fonts.googleapis.com/css2?family=Raleway:wght@400;500;600;800&display=swap" rel="stylesheet">
<style>
  :root{
    --purple:#6a2a6c;
    --purple-soft:#b48cc0;
    --teal:#7ab7b2;
    --teal-light:#b6dcdc;
    --ink:#1f1f1f;
    --muted:#444;
    --hero-bg:#eeeef0;
    --white:#ffffff;
  }
  *{box-sizing:border-box;margin:0;padding:0}
  html,body{width:1200px;height:890px;overflow:hidden;background:var(--white);font-family:"Raleway",sans-serif;color:var(--ink)}
  .topbar{height:30px;background:var(--purple);display:flex;align-items:center;justify-content:space-between;padding:0 300px 0 205px}
  .social{display:flex;gap:10px}
  .social span{width:11px;height:11px;border-radius:50%;background:var(--white);display:block}
  .account{display:flex;gap:14px;color:var(--white);font-size:11px}
  .site-header{height:110px;display:flex;align-items:center;padding:0 0 0 195px}
  .brand{display:flex;align-items:center;gap:10px;width:225px}
  .brand-mark{width:22px;height:22px;background:var(--teal)}
  .brand-name{font-size:20px;font-weight:600;color:var(--ink)}
  .nav{display:flex;gap:16px;font-size:10.5px}
  .nav a{color:var(--ink);text-decoration:none}
  .nav a.active{color:var(--purple);border-bottom:2px solid var(--teal);padding-bottom:3px}
  .header-icons{display:flex;gap:20px;margin-left:26px}
  .hero{position:relative;height:620px;display:flex;background:var(--hero-bg)}
  .hero-photo{width:520px;height:100%;background:linear-gradient(135deg,#5a4a42 0%,#cfd2d2 35%,#eef0f0 55%,#6b5c52 80%,#3b3330 100%)}
  .hero-copy{padding:140px 0 0 40px;flex:1}
  .hero-title{font-size:31px;font-weight:800;letter-spacing:-.2px;text-transform:uppercase}
  .hero-sub{font-size:20px;font-weight:500;margin-top:2px}
  .quote{font-size:12px;line-height:1.45;width:380px;margin-top:32px;color:var(--ink)}
  .author{font-size:14px;margin-top:14px}
  .stars{display:flex;gap:5px;margin-top:12px}
  .avatar{width:84px;height:84px;border-radius:50%;background:linear-gradient(160deg,#e9e4e0,#8a6f62);border:1px solid #ccc;margin-top:18px}
  .cta{display:inline-flex;align-items:center;gap:16px;margin-top:24px;background:var(--purple-soft);color:var(--white);border-radius:24px;padding:5px 5px 5px 18px;font-size:15px;text-decoration:none}
  .cta-arrow{width:38px;height:38px;border-radius:50%;background:var(--white);display:flex;align-items:center;justify-content:center}
  .pager{position:absolute;right:50px;top:345px;display:flex;flex-direction:column;align-items:center;gap:8px}
  .pager span{width:8px;height:8px;border-radius:50%;border:2px solid var(--teal)}
  .pager span.on{width:14px;height:14px;border-color:var(--ink)}
  .next-section{display:flex;height:130px}
  .next-section .blank{flex:1}
  .next-photo{width:520px;background:linear-gradient(180deg,var(--teal-light),#9fc9c9)}
</style>
</head>
<body>
  <div class="topbar">
    <div class="social"><span></span><span></span><span></span><span></span><span></span></div>
    <div class="account"><span>Log in / Register</span><span>Wishlist</span></div>
  </div>
  <header class="site-header">
    <div class="brand">
      <div class="brand-mark"></div>
      <div class="brand-name">GlassVela</div>
    </div>
    <nav class="nav">
      <a class="active" href="#">Home</a>
      <a href="#">Shop Mirror Frames</a>
      <a href="#">Custom Frames Mirrors</a>
      <a href="#">How It Works</a>
      <a href="#">Before &amp; After Gallery</a>
    </nav>
    <div class="header-icons">
      <svg width="18" height="18" viewBox="0 0 18 18" fill="none" stroke="#222" stroke-width="1.8"><circle cx="7.5" cy="7.5" r="5.5"/><path d="M11.5 11.5l5 5"/></svg>
      <svg width="16" height="18" viewBox="0 0 16 18" fill="none" stroke="#222" stroke-width="1.6"><rect x="1.5" y="5" width="13" height="12" rx="1"/><path d="M5 5V4a3 3 0 0 1 6 0v1"/></svg>
    </div>
  </header>
  <section class="hero">
    <div class="hero-photo" role="img" aria-label="Bathroom vanity with two large dark-framed mirrors, white flowers and pendant lights"></div>
    <div class="hero-copy">
      <h1 class="hero-title">Frame any mirror in your house</h1>
      <p class="hero-sub">with an elegant custom cut frame</p>
      <p class="quote">"Great product and great service! Adding frames to our mirrors made all the difference in how the master bath looks. You can't beat GlassVela for the money!"</p>
      <p class="author">- Dana R., Carlsbad, CA</p>
      <div class="stars">
        <svg width="90" height="14" viewBox="0 0 90 14" fill="#7ab7b2"><g id="s"><path d="M7 0l2 4.5 5 .5-3.8 3.3 1.1 4.9L7 10.8 2.7 13.2l1.1-4.9L0 5l5-.5z"/></g><use href="#s" x="19"/><use href="#s" x="38"/><use href="#s" x="57"/><use href="#s" x="76"/></svg>
      </div>
      <div class="avatar" role="img" aria-label="Portrait of the reviewing customer"></div>
      <a class="cta" href="#">Get free Sample Code
        <span class="cta-arrow"><svg width="20" height="16" viewBox="0 0 20 16" fill="none" stroke="#2a1030" stroke-width="2.4"><path d="M1 8h16M11 2l6 6-6 6"/></svg></span>
      </a>
    </div>
    <div class="pager"><span></span><span class="on"></span><span></span><span></span></div>
  </section>
  <section class="next-section">
    <div class="blank"></div>
    <div class="next-photo" role="img" aria-label="Bright bathroom with pale teal walls and brass light fixtures"></div>
  </section>
</body>
</html>
```